Driving School Business card design

Hi, we are starting a new business (Driving School) and would like your help with our business card design.
We are located in Adelaide SA.
Our aim is to help young people achieve best possible results by promoting safe and stress free driving.

Name of our school is "Brindle" which means best or most favorable.

Hope there is someone out there in wonderful world of design who can think outside of square and give us recognizable/ unique business card design.

Target Market(s)

16+

Industry/Entity Type

Business

Contact Information for Business Card

Name of our business is "Brindle driver training"
Our idea is to make letter "L' in Brindle more distinct (noticeable) by different color or font, so it gets associated with learner driver.
We like combination of white, dark gray and yellow but do not limit our self to that.
Reverse side of our card would have to incorporate writing space for date and time of the next lesson.

Requirements
Must have
• Business name: Brindle driver training
• Owner/ instructor name
• Mobile no:
• Loopnest logo
Should not have
• Anything Not associated with driving

```html
<!DOCTYPE html>
<html lang="en">
<head>
<meta charset="utf-8">
<title>Brindle Driver Training – Business Card</title>
<link rel="stylesheet" href="https://fonts.googleapis.com/css2?family=Poppins:wght@400;500;600;700&display=swap">
<style>
  :root {
    --stage: #2b2b2d;
    --card-dark: #1d2226;
    --charcoal: #3a3a3c;
    --white: #ffffff;
    --lime: #d4e81c;
    --ink: #3d3d3f;
    --muted: #6a6a6c;
    --rule: #b9b9bb;
  }
  * { box-sizing: border-box; margin: 0; padding: 0; }
  html, body { width: 1200px; height: 900px; overflow: hidden; }
  body {
    background: var(--stage);
    font-family: "Poppins", Arial, sans-serif;
    position: relative;
  }
  .card {
    position: absolute;
    width: 520px;
    height: 300px;
    border-radius: 22px;
    overflow: hidden;
    box-shadow: 0 18px 40px rgba(0,0,0,0.45);
  }

  /* Wordmark: name set in one colour and weight, learner square beside it */
  .wordmark { position: absolute; display: flex; align-items: flex-start; }
  .wordmark-name { font-weight: 700; line-height: 1; letter-spacing: -1px; }
  .learner-square { background: var(--lime); flex: none; }

  /* Front (photo side) */
  .card--front { left: 70px; top: 130px; background: var(--card-dark); }
  .front-photo {
    position: absolute; inset: 0;
    background: linear-gradient(160deg, #3b4650 0%, #2a3138 38%, #1f2a22 62%, #15191c 100%);
  }
  .front-content { position: absolute; inset: 0; color: var(--white); }
  .front-wordmark { left: 78px; top: 58px; }
  .front-wordmark .wordmark-name { font-size: 84px; color: var(--white); }
  .front-wordmark .learner-square { width: 20px; height: 20px; margin: 14px 0 0 8px; }
  .front-tagline {
    position: absolute; right: 92px; top: 146px;
    font-size: 15px; font-weight: 500; letter-spacing: 5px;
    color: var(--white);
  }
  .social {
    position: absolute; left: 0; right: 0; top: 186px;
    display: flex; justify-content: center; align-items: center; gap: 8px;
  }
  .social-square { width: 22px; height: 22px; background: #3d5a98; border-radius: 3px; }
  .social-name { font-size: 15px; font-weight: 500; color: var(--white); }
  .front-web {
    position: absolute; left: 0; right: 0; top: 236px; text-align: center;
    font-size: 16px; font-weight: 500; color: var(--white);
  }
  .front-web .web-name { color: var(--lime); font-weight: 600; }

  /* Back (contact side) */
  .card--back { left: 610px; top: 470px; background: var(--white); }
  .back-shapes { position: absolute; inset: 0; }
  .back-wordmark { left: 236px; top: 20px; }
  .back-wordmark .wordmark-name { font-size: 52px; color: var(--ink); }
  .back-wordmark .learner-square { width: 13px; height: 13px; margin: 9px 0 0 6px; }
  .back-tagline {
    position: absolute; right: 66px; top: 76px;
    font-size: 10px; font-weight: 500; letter-spacing: 3px; color: var(--muted);
  }

  .next-lesson { position: absolute; left: 30px; top: 26px; width: 180px; }
  .next-lesson-title {
    font-size: 10px; font-weight: 600; letter-spacing: 2px; color: var(--ink);
    margin-bottom: 6px;
  }
  .next-lesson-field {
    display: flex; align-items: flex-end; gap: 8px;
    font-size: 11px; color: var(--muted); height: 24px;
  }
  .next-lesson-line { flex: 1; border-bottom: 1px solid var(--rule); height: 16px; }

  .contact { position: absolute; left: 30px; top: 136px; }
  .contact-name {
    font-size: 19px; font-weight: 700; color: var(--lime); letter-spacing: 0.5px; line-height: 26px;
  }
  .contact-role { font-size: 11px; color: var(--ink); margin-bottom: 4px; letter-spacing: 0.5px; }
  .contact-list { list-style: none; }
  .contact-list li {
    display: flex; align-items: center; gap: 8px;
    font-size: 13px; color: var(--ink); line-height: 20px;
  }
  .contact-list svg { width: 11px; height: 11px; flex: none; }
</style>
</head>
<body>

  <section class="card card--front">
    <div class="front-photo" role="img" aria-label="Photo of a winding coastal road with guard rail and trees at dusk"></div>
    <div class="front-content">
      <div class="wordmark front-wordmark">
        <span class="wordmark-name">Brindle</span>
        <span class="learner-square"></span>
      </div>
      <div class="front-tagline">DRIVER TRAINING</div>
      <div class="social">
        <span class="social-square"></span>
        <span class="social-name">Loopnest</span>
      </div>
      <div class="front-web">www.<span class="web-name">brindledrivertraining</span>.com</div>
    </div>
  </section>

  <section class="card card--back">
    <svg class="back-shapes" viewBox="0 0 520 300" width="520" height="300" aria-hidden="true">
      <circle cx="425" cy="160" r="70" fill="var(--charcoal)"/>
      <polygon points="380,232 412,200 520,200 520,224 400,224" fill="var(--lime)"/>
      <polygon points="0,258 352,258 392,224 520,224 520,300 0,300" fill="var(--charcoal)"/>
    </svg>

    <div class="next-lesson">
      <div class="next-lesson-title">NEXT LESSON</div>
      <div class="next-lesson-field"><span>Date</span><span class="next-lesson-line"></span></div>
      <div class="next-lesson-field"><span>Time</span><span class="next-lesson-line"></span></div>
    </div>

    <div class="wordmark back-wordmark">
      <span class="wordmark-name">Brindle</span>
      <span class="learner-square"></span>
    </div>
    <div class="back-tagline">DRIVER TRAINING</div>

    <div class="contact">
      <div class="contact-name">MARCUS HALE</div>
      <div class="contact-role">OWNER</div>
      <ul class="contact-list">
        <li>
          <svg viewBox="0 0 12 12"><rect x="3" y="0.5" width="6" height="11" rx="1.2" fill="none" stroke="var(--lime)" stroke-width="1.3"/><circle cx="6" cy="9.5" r="0.8" fill="var(--lime)"/></svg>
          +330 2417-6093
        </li>
        <li>
          <svg viewBox="0 0 12 12"><rect x="0.7" y="2.2" width="10.6" height="7.6" fill="none" stroke="var(--lime)" stroke-width="1.3"/><polyline points="0.7,2.4 6,6.6 11.3,2.4" fill="none" stroke="var(--lime)" stroke-width="1.3"/></svg>
          info@brindledrivertraining.com
        </li>
        <li>
          <svg viewBox="0 0 12 12"><circle cx="6" cy="6" r="5.2" fill="none" stroke="var(--lime)" stroke-width="1.3"/><ellipse cx="6" cy="6" rx="2.2" ry="5.2" fill="none" stroke="var(--lime)" stroke-width="1"/><line x1="0.8" y1="6" x2="11.2" y2="6" stroke="var(--lime)" stroke-width="1"/></svg>
          www.brindledrivertraining.com
        </li>
      </ul>
    </div>
  </section>

</body>
</html>
```